Flyer Design

I will be hosting an event at Penrith's open workroom. Here is a link to their page http://www.theopenworkroom.com.au/events-and-workshops/whats-on-penrith/. I have attached the details of my course from their website below. I hope this is of some valuable assistance.

Florist and lover of all things gorgeous, Molly Brandt from Molly Brandt Flowers will be running this beautiful and fun workshop. Come along to learn how to make your very own floral crown. All you need to bring are some closed in shoes, an apron and an open mind ready for creativity!

Teens & adults welcome

Date 1: Saturday 11 April 2015
Time 1: 11:00-2:00pm

Date 2: Thursday 23 April 2015
Time 2: 6:00-9:00pm

Cost: $90 per person (includes materials provided – see list below)
Place: The Open Workroom, Unit 3, 17 Holloway Street Penrith
RSVP: Molly via email mollybrandtflowers@postvale.com or phone 0431 507 962

Materials provided:
• Florist scissors
• Parafilm
• Wire
• Flowers
• light snacks & refreshments

```html
<!DOCTYPE html>
<html lang="en">
<head>
<meta charset="utf-8">
<title>Floral Crowns Workshop – Flyer</title>
<link href="https://fonts.googleapis.com/css2?family=Great+Vibes&family=PT+Sans:ital,wght@0,400;0,700;1,400&family=Raleway:wght@300;400&display=swap" rel="stylesheet">
<style>
  :root{
    --page:#ffffff;
    --plum-dark:#4f3a68;
    --plum:#5e4679;
    --plum-band:#7c6494;
    --magenta:#c9589f;
    --pink-text:#d55aa6;
    --pink-light:#f3b7dd;
    --lavender:#e6e0ef;
    --ink:#2c2434;
    --gold:#f2e15a;
    --silver:#f2f0f4;
  }
  *{box-sizing:border-box;margin:0;padding:0}
  html,body{width:1200px;height:900px;overflow:hidden;background:var(--page)}
  .canvas{position:relative;width:1200px;height:900px;font-family:"PT Sans",sans-serif;color:var(--ink)}
  .flyer{position:absolute;left:330px;top:12px;width:590px;height:830px;overflow:hidden;background:var(--lavender);
    box-shadow:0 4px 14px rgba(0,0,0,.18)}
  .abs{position:absolute}
  .header-photo{left:0;top:0;width:590px;height:360px;
    background:radial-gradient(circle at 120px 200px,rgba(255,230,245,.75) 0,rgba(230,150,200,.35) 90px,transparent 200px),
               linear-gradient(100deg,#5a2f5e 0%,#8c4a84 30%,#b87aa8 55%,#6d4a7c 80%,#3d2c4c 100%)}
  .portrait{left:370px;top:30px;width:220px;height:330px;
    background:linear-gradient(180deg,#e9dadd 0%,#d8b8a8 35%,#c9a79e 60%,#a88a9c 100%);opacity:.9}
  .flower-photo{left:0;top:340px;width:190px;height:490px;
    background:linear-gradient(160deg,#5f8a43 0%,#b8d36a 30%,#f4f2d9 52%,#8aa65a 72%,#3c5a2a 100%)}
  .title-script{left:12px;top:82px;font-family:"Great Vibes",cursive;font-size:64px;color:var(--silver);
    text-shadow:0 2px 3px rgba(60,20,60,.6);white-space:nowrap;transform:rotate(-4deg)}
  .title-caps{left:22px;top:164px;font-family:"Raleway",sans-serif;font-weight:300;font-size:44px;letter-spacing:.36em;
    color:var(--silver);text-shadow:0 2px 3px rgba(60,20,60,.5)}
  .tagline{left:12px;top:258px;width:380px;text-align:center;font-family:"Great Vibes",cursive;font-size:27px;color:#fff;
    transform:rotate(-10deg);white-space:nowrap}
  .badge-text{left:452px;top:276px;width:120px;text-align:center;font-weight:700;color:#fff;font-size:18px;line-height:19px;
    transform:rotate(-18deg);text-shadow:0 1px 2px rgba(0,0,0,.4)}
  .intro{left:110px;top:364px;width:460px;text-align:center;font-size:18px;line-height:23px}
  .come-along{left:218px;top:422px;color:#fff;font-size:17px;line-height:22px}
  .come-along .lead{color:var(--pink-light);font-size:25px}
  .bring{left:192px;top:482px;font-size:18px;line-height:23px}
  .materials-title{left:200px;top:545px;color:var(--pink-text);font-weight:700;font-size:17px;text-decoration:underline;letter-spacing:.02em}
  .materials-list{left:197px;top:577px;list-style:none;font-size:17px}
  .materials-list li{height:33px}
  .date{width:110px;text-align:center;color:#fff;font-weight:700;font-size:15px}
  .date span{display:block;line-height:17px;white-space:nowrap}
  .date .label{color:var(--gold);font-weight:400;font-size:11px;line-height:14px;text-decoration:underline}
  .date-one{left:411px;top:549px}
  .date-two{left:458px;top:655px}
  .footer{left:0;top:768px;width:590px;text-align:center;color:#fff;font-size:12.5px;line-height:17px;padding-left:70px}
  .footer .label{color:var(--gold)}
</style>
</head>
<body>
<div class="canvas">
  <div class="flyer">
    <div class="abs header-photo" role="img" aria-label="Soft purple and pink bokeh light background"></div>
    <div class="abs portrait" role="img" aria-label="Photo of a young woman wearing a floral crown"></div>

    <svg class="abs" style="left:0;top:0" width="590" height="830" viewBox="0 0 590 830">
      <path d="M0 0H590V24Q300 48 0 24Z" fill="var(--plum)"/>
      <path d="M0 26Q300 50 590 26" fill="none" stroke="#fff" stroke-width="3"/>
      <path d="M0 335L310 335Q420 318 590 362V830H0Z" fill="var(--lavender)"/>
      <path d="M0 335Q160 345 290 328Q420 318 590 362" fill="none" stroke="#fff" stroke-width="4"/>
      <polygon points="0,280 395,214 372,268 394,298 0,350" fill="var(--magenta)"/>
      <polygon points="395,214 372,268 394,298 380,250" fill="#9d3f7f" opacity=".5"/>
      <g transform="translate(512,306)">
        <polygon fill="var(--plum)" stroke="#fff" stroke-width="2"
          points="0,-62 13,-46 33,-53 33,-33 53,-30 44,-12 60,2 44,14 52,33 32,35 31,56 12,48 0,63 -12,48 -31,56 -32,35 -52,33 -44,14 -60,2 -44,-12 -53,-30 -33,-33 -33,-53 -13,-46"/>
        <polygon fill="#d8a6d6" opacity=".6" points="-60,2 -44,-12 -53,-30 -33,-33 -33,-53 -13,-46 0,-62 13,-46 10,0"/>
      </g>
    </svg>

    <div class="abs flower-photo" role="img" aria-label="Photo of a bouquet of white roses and green flowers"></div>

    <div class="abs title-script">Floral Crowns</div>
    <div class="abs title-caps">WORKSHOP</div>
    <div class="abs tagline">Florist and lover of all things gorgeous</div>
    <div class="abs badge-text">TEENS<br>&amp; ADULTS<br>WELCOME</div>

    <p class="abs intro">Molly Brandt from Molly Brandt Flowers will be<br>running this beautiful and fun workshop.</p>

    <svg class="abs" style="left:178px;top:418px" width="412" height="56" viewBox="0 0 412 56">
      <polygon points="0,0 412,0 412,56 22,56 40,28" fill="var(--plum-band)"/>
    </svg>
    <p class="abs come-along"><span class="lead">COME ALONG</span> to learn how to make<br>your very own <i>floral crown.</i></p>

    <p class="abs bring">All you need to bring are some closed in shoes,<br>an apron and an open mind ready for creativity!</p>

    <h2 class="abs materials-title">MATERIALS PROVIDED:</h2>
    <ul class="abs materials-list">
      <li>• Florist scissors</li>
      <li>• Parafilm</li>
      <li>• Wire</li>
      <li>• Flowers</li>
      <li>• light snacks &amp; refreshments</li>
    </ul>

    <svg class="abs" style="left:390px;top:520px" width="200" height="250" viewBox="0 0 200 250">
      <circle cx="80" cy="73" r="58" fill="#8d7aa3" opacity=".5"/>
      <circle cx="76" cy="68" r="58" fill="var(--plum)" stroke="#fff" stroke-width="3"/>
      <circle cx="127" cy="178" r="58" fill="#8d7aa3" opacity=".5"/>
      <circle cx="123" cy="173" r="58" fill="var(--plum)" stroke="#fff" stroke-width="3"/>
    </svg>
    <div class="abs date date-one">
      <span class="label">Date 1:</span><span>Saturday</span><span>11 April 2015</span>
      <span class="label">Time 1:</span><span>11:00-2:00pm</span>
    </div>
    <div class="abs date date-two">
      <span class="label">Date 2:</span><span>Thursday</span><span>23 April 2015</span>
      <span class="label">Time 2:</span><span>6:00-9:00pm</span>
    </div>

    <svg class="abs" style="left:0;top:760px" width="590" height="70" viewBox="0 0 590 70">
      <path d="M0 12Q300 -4 590 8V70H0Z" fill="var(--plum-dark)"/>
      <path d="M0 12Q300 -4 590 8" fill="none" stroke="#fff" stroke-width="2"/>
    </svg>
    <div class="abs footer">
      <span class="label">Cost:</span> $90 per person (includes materials provided – see list below)<br>
      <span class="label">Place:</span> The Open Workroom, Unit 3, 17 Holloway Street Penrith<br>
      <span class="label">RSVP:</span> Molly via email mollybrandtflowers@postvale.com or phone 0431 507 962
    </div>
  </div>
</div>
</body>
</html>
```